Key Scientific Research Plastics Presentation - 5 Slides

We need the attached slides reworked with the following changes:

Information needs to be very visually stunning and easily understood
Text/font treatments should attract attention
All graphs and infographics can be recreated to match style
Attached color palette is not necessary, but can be used

Please reach out with any questions.

```html
<!DOCTYPE html>
<html lang="en">
<head>
<meta charset="utf-8">
<title>Key Scientific Research – Plastics Presentation</title>
<link href="https://fonts.googleapis.com/css2?family=Poppins:ital,wght@0,300;0,400;0,500;0,600;0,700;1,400;1,600&family=Roboto:ital,wght@0,400;0,500;0,700;1,400;1,700&display=swap" rel="stylesheet">
<style>
:root{
  --canvas:#8c8c8c;
  --slide:#fafafa;
  --gold:#b98a0c;
  --olive:#9ea616;
  --brown:#5a2914;
  --ink:#222222;
  --muted:#444444;
  --sky:#5c9bd6;
  --navy:#2d5faa;
  --orange:#f4a52a;
  --link:#5a86c4;
  --white:#ffffff;
}
*{box-sizing:border-box;margin:0;padding:0}
html,body{width:1200px;height:3398px;overflow:hidden}
body{background:var(--canvas);font-family:"Roboto",sans-serif;color:var(--ink);position:relative}
.slide{position:absolute;left:61px;width:1078px;height:607px;background:var(--slide);box-shadow:0 2px 6px rgba(0,0,0,.25);overflow:hidden}
.abs{position:absolute}
.accent-bars{position:absolute;left:54px;top:22px;display:flex;gap:17px}
.accent-bars span{display:block;width:46px;height:4px;border-radius:2px;background:var(--gold)}
.accent-bars span+span{background:var(--olive)}
.title{position:absolute;left:54px;top:42px;font-family:"Poppins",sans-serif;font-weight:400;font-size:35px;line-height:44px;color:var(--ink)}
.title b{font-weight:700;color:var(--brown)}
.brand{position:absolute;left:847px;top:34px;display:flex;align-items:center;gap:10px}
.brand-mark{width:98px;height:98px;border-radius:50%;background:var(--gold)}
.brand-name{font-family:"Poppins",sans-serif;font-weight:400;font-size:18px;line-height:20px;color:var(--brown)}
.page-no{position:absolute;left:1000px;top:566px;width:25px;height:25px;border-radius:50%;background:var(--olive);color:var(--white);font-family:"Poppins",sans-serif;font-weight:600;font-size:14px;line-height:25px;text-align:center}

/* slide 1 */
.question-box{position:absolute;left:54px;top:150px;width:606px;height:385px;background:var(--gold);border-radius:10px;padding:8px}
.question-box .inner{border:1.5px dashed rgba(255,255,255,.75);border-radius:8px;height:100%;padding:26px 18px 0 22px}
.question-list{list-style:none;color:var(--white);font-size:16px;line-height:42px}
.question-list li{display:flex;align-items:flex-start;gap:12px}
.question-list li .txt{flex:1}
.q-icon{flex:none;width:22px;height:22px;border-radius:50%;background:rgba(255,255,255,.3);margin-top:10px;display:flex;align-items:center;justify-content:center;color:var(--white);font-size:13px;font-weight:700;line-height:1}
.q-icon svg{width:12px;height:12px}
.point-list{position:absolute;left:693px;top:172px;width:360px;list-style:none;font-size:20px;line-height:42px;color:var(--ink)}
.point-list li{padding-left:24px;position:relative}
.point-list li::before{content:"";position:absolute;left:0;top:16px;width:11px;height:11px;border-radius:50%;background:var(--gold)}
.tagline{position:absolute;left:0;width:1078px;top:557px;text-align:center;font-family:"Poppins",sans-serif;font-weight:700;font-size:24px;color:var(--olive)}

/* slide 2 */
.intro{position:absolute;left:54px;top:98px;width:760px;font-size:16px;line-height:27px;color:var(--ink)}
.intro b{font-weight:700}
.card{position:absolute;top:190px;width:410px;height:352px;border-radius:24px;color:var(--white);padding:0 16px}
.card.gold{left:108px;background:var(--gold)}
.card.olive{left:558px;background:var(--olive)}
.card-badge{position:absolute;left:161px;top:21px;width:88px;height:95px;background:var(--white);display:flex;align-items:center;justify-content:center;text-align:center;font-family:"Roboto",sans-serif;font-weight:700;font-size:11px;line-height:14px;color:var(--brown);padding:6px}
.card-doc{position:absolute;left:163px;top:21px;width:88px;height:95px;background:linear-gradient(#ffffff,#e8e8e8);border:1px solid #ddd}
.card-text{position:absolute;left:12px;right:12px;top:133px;font-size:12.5px;line-height:24px}
.card-text p{padding-left:16px;position:relative}
.card-text p.bul::before{content:"";position:absolute;left:0;top:8px;width:8px;height:8px;border-radius:50%;background:var(--white)}
.card-text .lead{font-weight:700;font-size:16px}
.card-text b{font-weight:700}
.source{position:absolute;left:54px;top:570px;font-size:13.5px;font-weight:500;color:var(--ink)}

/* slide 3 */
.subtitle{position:absolute;left:54px;top:140px;font-size:19px;line-height:30px;color:var(--ink)}
.icon-ring{position:absolute;width:66px;height:66px;border-radius:50%;border:1.5px solid var(--gold);display:flex;align-items:center;justify-content:center}
.icon-ring.brown{border-color:var(--brown)}
.icon-ring svg{width:30px;height:30px}
.info-block{position:absolute;font-size:13.5px;line-height:26px;color:var(--ink)}
.info-block h3{font-family:"Poppins",sans-serif;font-weight:600;font-size:18px;line-height:24px;margin-bottom:2px;color:var(--ink)}
.info-block .dot{display:inline-block;width:7px;height:7px;border-radius:50%;background:var(--olive);margin-right:4px;vertical-align:1px}
.info-block .dot.brown{background:var(--brown)}
.finding-box{position:absolute;left:579px;top:360px;width:446px;height:182px;border-radius:18px;background:var(--gold);color:var(--white);font-style:italic;font-size:13.5px;line-height:25.5px;padding:24px 28px}
.finding-box b{font-weight:700}

/* slide 4 */
.lede{position:absolute;left:54px;top:136px;width:660px;font-size:13.5px;line-height:20px;color:var(--ink)}
.spine{position:absolute;left:270px;top:243px;width:4px;height:300px;background:var(--gold)}
.spine-dot{position:absolute;left:266px;top:540px;width:12px;height:12px;border-radius:50%;background:var(--gold)}
.spine-top{position:absolute;left:236px;top:191px;width:72px;height:72px;border-radius:50%;background:var(--gold)}
.pill{position:absolute;width:212px;height:52px;border-radius:26px;display:flex;align-items:center;gap:14px;padding-left:8px;color:var(--white);font-family:"Poppins",sans-serif;font-weight:600;font-size:16px}
.pill .knob{width:36px;height:36px;border-radius:50%;background:rgba(255,255,255,.92);display:flex;align-items:center;justify-content:center}
.pill .knob svg{width:20px;height:20px}
.pill.dose{left:59px;top:285px;background:var(--olive)}
.pill.toxicity{left:270px;top:330px;background:var(--sky)}
.pill.duration{left:59px;top:380px;background:var(--navy)}
.pill.frequency{left:270px;top:430px;background:var(--orange)}
.pill.route{left:59px;top:482px;background:var(--brown);font-size:15px}
.ratings-caption{position:absolute;left:100px;width:340px;top:563px;text-align:center;font-family:"Poppins",sans-serif;font-weight:500;font-size:16px;color:var(--ink)}
.hazard{position:absolute;left:576px;top:182px;width:440px;font-size:11.5px;line-height:20px;color:var(--ink)}
.hazard h3{font-family:"Poppins",sans-serif;font-weight:600;font-size:24px;line-height:30px;margin-bottom:8px}
.hazard h4{font-weight:500;font-size:13px;line-height:20px;margin-top:16px}
.hazard .note{font-style:italic;color:var(--link);margin-top:20px}
.hazard .caution{margin-top:20px;color:#555}

/* slide 5 */
.sub-5{position:absolute;left:56px;top:146px;font-size:16.5px;color:var(--ink)}
.dose-table{position:absolute;left:54px;top:214px;width:451px;height:327px;border-collapse:collapse;font-size:16px;color:var(--ink);border:1px solid #777}
.dose-table th{background:var(--gold);color:var(--white);font-weight:400;font-size:13.5px;line-height:20px;height:50px;text-align:center}
.dose-table td{text-align:center;border-top:1px solid #999;line-height:24px}
.dose-table th+th,.dose-table td+td{border-left:1px solid #999}
.chart{position:absolute;left:560px;top:225px;width:480px;height:310px}
</style>
</head>
<body>

<!-- Slide 1 -->
<section class="slide" style="top:55px">
  <div class="accent-bars"><span></span><span></span></div>
  <h1 class="title">WEA Plastic Pollution Treaty<br><b>Scientific Checks &amp; Balances</b></h1>
  <div class="brand"><div class="brand-mark"></div><div class="brand-name">Polyfoam<br>Council</div></div>

  <div class="question-box"><div class="inner">
    <ul class="question-list">
      <li><span class="q-icon"><svg viewBox="0 0 12 12"><path d="M2 6l3 3 5-6" fill="none" stroke="#fff" stroke-width="2"/></svg></span><span class="txt">The Body of Research on Plastic Is Extensive.</span></li>
      <li><span class="q-icon">?</span><span class="txt">Are All Plastics Toxic?</span></li>
      <li><span class="q-icon">?</span><span class="txt">Are NGO, WEA or Industry Interpretations Accurate or Inaccurate?</span></li>
      <li><span class="q-icon"><svg viewBox="0 0 12 12"><path d="M3 3l6 6M9 3l-6 6" fill="none" stroke="#fff" stroke-width="2"/></svg></span><span class="txt">Is Data Transparency Evident For The Science Supporting Policy Considerations?</span></li>
      <li><span class="q-icon">?</span><span class="txt">Problematic Plastics Are Classified Without Criteria</span></li>
      <li><span class="q-icon"><svg viewBox="0 0 12 12"><path d="M2 6l3 3 5-6" fill="none" stroke="#fff" stroke-width="2"/></svg></span><span class="txt">Is Scientific Information On Plastic Pollution Being Used Out Of Context?</span></li>
    </ul>
  </div></div>

  <ul class="point-list">
    <li>Some think science can provide definitive, complete and foolproof answers.</li>
    <li>But given the world’s complexity, different research modalities and replication limits, critical thinking must be embraced to develop policies that work.</li>
  </ul>

  <p class="tagline">Know How To Ask The Right Questions</p>
  <div class="page-no">1</div>
</section>

<!-- Slide 2 -->
<section class="slide" style="top:721px">
  <div class="accent-bars"><span></span><span></span></div>
  <h1 class="title">NGO Misuse of <b>Technical Data</b></h1>
  <div class="brand"><div class="brand-mark"></div><div class="brand-name">Polyfoam<br>Council</div></div>
  <p class="intro">The definition of data misuse is <b>using any information in a way it’s not supposed to be used.</b> Terms of proper data use are usually specified in laws, industry standards, policies, and other agreements.</p>

  <div class="card gold">
    <div class="card-badge">Coastal Waste Watch</div>
    <div class="card-text">
      <p class="bul"><span class="lead">False Claim:</span> “Polystyrene foam contains styrene, which has been <b>linked to cancer, vision and hearing loss,</b> impaired memory and concentration, &amp; nervous system effects.”</p>
      <p class="bul" style="margin-top:12px"><span class="lead">Reference:</span> Potential Toxicity of Polystyrene Microplastics</p>
    </div>
  </div>

  <div class="card olive">
    <div class="card-doc" role="img" aria-label="First page of the journal article on polystyrene microplastic toxicity"></div>
    <div class="card-text">
      <p class="bul"><span class="lead">Research Conclusions:</span> “The study confirmed that <b>PS particles were not toxic to human cells</b> at a dosage of <b>~500µg/mL</b> and PS particles with diameters of <b>10-11</b> µm were not <b>significantly cytotoxic</b>”. Further,</p>
      <p style="margin-top:12px">“It could be concluded that PS particles are not cytotoxic to <b>HDFs and PBMCs</b> in usual conditions but might cause damage in extreme, <b>high concentrations.</b>”</p>
    </div>
  </div>

  <p class="source">Potential Toxicity of Polystyrene Microplastic Particles, Hanwol University, South Korea&nbsp; December 1, 2020</p>
  <div class="page-no">2</div>
</section>

<!-- Slide 3 -->
<section class="slide" style="top:1386px">
  <div class="accent-bars"><span></span><span></span></div>
  <h1 class="title" style="top:44px">Atmospheric Studies In <b>11 Cities</b><br><b>Have Varying Results</b></h1>
  <div class="brand"><div class="brand-mark"></div><div class="brand-name">Polyfoam<br>Council</div></div>
  <p class="subtitle">Does Microplastic Really Represent A Threat? A Review of Atmospheric Contamination<br>Sources &amp; Potential Impacts (2021)</p>

  <div class="icon-ring" style="left:54px;top:224px"><svg viewBox="0 0 30 30" fill="none" stroke="#b98a0c" stroke-width="1.5"><circle cx="13" cy="12" r="8"/><path d="M13 20v6M9 26h8M20 9l5-3"/></svg></div>
  <div class="info-block" style="left:137px;top:222px;width:400px">
    <h3>Thematic Hypothesis:</h3>
    <p><span class="dot"></span>Atmospheric transport of microplastics is detrimental and is of great concern to the global community.</p>
  </div>

  <div class="icon-ring brown" style="left:560px;top:224px"><svg viewBox="0 0 30 30" fill="none" stroke="#5a2914" stroke-width="1.5"><circle cx="12" cy="17" r="7"/><circle cx="21" cy="9" r="4"/><path d="M12 14v6M9 17h6"/></svg></div>
  <div class="info-block" style="left:644px;top:222px;width:390px">
    <h3>Bottom Line:</h3>
    <p><span class="dot brown"></span>There is a need to conduct comprehensive research on sources of atmospheric microplastics to aid in the initiation of effective control mechanisms and policy measures.</p>
  </div>

  <div class="icon-ring" style="left:54px;top:347px"><svg viewBox="0 0 30 30" fill="none" stroke="#b98a0c" stroke-width="1.5"><circle cx="15" cy="15" r="6"/><circle cx="15" cy="15" r="11" stroke-dasharray="3 3"/></svg></div>
  <div class="info-block" style="left:137px;top:344px;width:400px">
    <h3>What’s Inside:</h3>
    <p><span class="dot"></span>There Are Three (3) Air Sampling Methodologies In This Developing Field of Study</p>
    <p><span class="dot"></span>No Standard Method Exists To Prepare Airborne Microplastic Test Samples</p>
    <p><span class="dot"></span>Visual Identification Methods Are Ineffective For Smaller Atmospheric Samples</p>
    <p><span class="dot"></span>Studies Have Shown a Dominant Number of Airborne Microplastics are Fibers (≤95%).</p>
  </div>

  <div class="finding-box">In 11 studies in specific locations (Europe, Asia, North America) <b>airborne polystyrene particles were found in only three cities.</b><br>The results represent three different test sample types and all three used varying air concentration calculations.</div>
  <div class="page-no">3</div>
</section>

<!-- Slide 4 -->
<section class="slide" style="top:2052px">
  <div class="accent-bars"><span></span><span></span></div>
  <h1 class="title" style="top:44px">Understanding Risk <b>Versus</b><br><b>Exposure</b></h1>
  <div class="brand"><div class="brand-mark"></div><div class="brand-name">Polyfoam<br>Council</div></div>
  <p class="lede">Any substance can be poisonous. Chemicals of concern must be evaluated&nbsp; within typical use parameters to evaluate its potential to present a hazard.</p>

  <div class="spine"></div>
  <div class="spine-dot"></div>
  <div class="spine-top"></div>

  <div class="pill dose"><span class="knob"><svg viewBox="0 0 20 20" fill="none" stroke="#9ea616" stroke-width="1.5"><rect x="3" y="4" width="14" height="10"/><path d="M6 11l3-3 2 2 3-4M10 14v3"/></svg></span>Dose</div>
  <div class="pill toxicity"><span class="knob"><svg viewBox="0 0 20 20" fill="none" stroke="#5c9bd6" stroke-width="1.5"><path d="M8 3h4M9 3v5l-5 8h12l-5-8V3"/></svg></span>Toxicity</div>
  <div class="pill duration"><span class="knob"><svg viewBox="0 0 20 20" fill="none" stroke="#2d5faa" stroke-width="1.5"><path d="M5 3h10M5 17h10M6 3c0 5 8 5 8 7s-8 2-8 7M14 3c0 5-8 5-8 7"/></svg></span>Duration</div>
  <div class="pill frequency"><span class="knob"><svg viewBox="0 0 20 20" fill="none" stroke="#f4a52a" stroke-width="1.5"><rect x="3" y="4" width="14" height="13"/><path d="M3 8h14M7 2v4M13 2v4"/></svg></span>Frequency</div>
  <div class="pill route"><span class="knob"><svg viewBox="0 0 20 20" fill="none" stroke="#5a2914" stroke-width="1.5"><rect x="3" y="4" width="14" height="12"/><path d="M6 12l3-4 2 3 3-4"/></svg></span>Route of Exposure</div>
  <p class="ratings-caption">Is It Toxic? Scientific Ratings</p>

  <div class="hazard">
    <h3>Carcinogens</h3>
    <p><b>“No significant risk level”</b> (“NSRL”) means that exposure to the amount of chemical in a product would result in no more than one case of cancer out of every 100,000 individuals who were exposed to the chemical over a 70-year time period.</p>
    <h4>Reproductive Toxins</h4>
    <p>Maximum allowable dose level (“MADL”) is the level at which a chemical would have no observable effect, even if an individual were exposed to 1,000 times that level</p>
    <p class="note">Risk Assessment Involves Reasonable Assumptions Under Different Exposure Scenarios To Determine Toxicity Levels</p>
    <p class="caution">National Risk Data System (NRDS) cautions that “NRDS values cannot be validly used to accurately predict the incidence of human disease or the type of effects that chemical exposures have on humans. This is due to the numerous uncertainties involved in risk assessment, including those associated with extrapolations from animal data to humans and from high experimental doses to lower environmental exposures.”</p>
  </div>
  <div class="page-no">4</div>
</section>

<!-- Slide 5 -->
<section class="slide" style="top:2717px">
  <div class="accent-bars"><span></span><span></span></div>
  <h1 class="title" style="top:44px">Expanded Polystyrene Does Not<br>Pose <b>A Human Health Threat</b></h1>
  <div class="brand"><div class="brand-mark"></div><div class="brand-name">Polyfoam<br>Council</div></div>
  <p class="sub-5">Expanded Polystyrene Foam – Residual Styrene Emissions</p>

  <table class="dose-table">
    <thead><tr><th style="width:225px">Exposure Scenario</th><th>Consumer Styrene Lifetime<br>Average Daily Dose µg/day</th></tr></thead>
    <tbody>
      <tr><td>Private Office</td><td>0.05-0.75</td></tr>
      <tr><td>School Classroom</td><td>0.03-0.48</td></tr>
      <tr><td>Home Residence</td><td>0.48-7.33</td></tr>
      <tr><td>SCHA Safe Harbor<br>Styrene NSRL</td><td>27</td></tr>
    </tbody>
  </table>

  <svg class="chart" viewBox="0 0 480 310" font-family="Roboto, sans-serif" font-size="10" fill="#333">
    <!-- baseline at y=281, 2.21 px per unit, x axis at 28 -->
    <g text-anchor="end">
      <text x="18" y="284">0</text><text x="18" y="240">20</text><text x="18" y="196">40</text>
      <text x="18" y="151">60</text><text x="18" y="107">80</text><text x="18" y="63">100</text><text x="18" y="19">120</text>
    </g>
    <line x1="28" y1="10" x2="28" y2="281" stroke="#999"/>
    <line x1="28" y1="281" x2="461" y2="281" stroke="#999"/>
    <g>
      <rect x="48" y="60" width="12" height="221" fill="#b98a0c"/>
      <rect x="67" y="82" width="12" height="199" fill="#9ea616"/>
      <rect x="171" y="170" width="12" height="111" fill="#b98a0c"/>
      <rect x="189" y="60" width="12" height="221" fill="#9ea616"/>
      <rect x="292" y="60" width="12" height="221" fill="#b98a0c"/>
      <rect x="311" y="82" width="12" height="199" fill="#9ea616"/>
    </g>
    <g text-anchor="middle" font-size="9.5">
      <text x="54" y="55">100</text><text x="75" y="77">90</text>
      <text x="177" y="165">50</text><text x="195" y="55">100</text>
      <text x="298" y="55">100</text><text x="317" y="77">90</text>
    </g>
    <g text-anchor="middle" font-size="10.5" font-weight="500">
      <text x="64" y="298">Office</text><text x="186" y="298">School</text><text x="308" y="298">Residence</text>
    </g>
  </svg>
  <div class="page-no">5</div>
</section>

</body>
</html>
```